Mirelle "Glass Tide" single cover

We need a cover for Mirelle's New upcoming single "Glass Tide"
We have posted some Pictures and logo that we want you to work With. We need you to get her to look good :).The title is "Glass Tide" and is "Mirelle feat. Tovro pip rascal"
The songs is a little hiphop/RnB (Norah K'ish).
You can choose what colour you want for the logo and overall. But we don't want it to be gloomy.
watch www.mirelle-example.no or www.sociabook.example/mirellemusic
This is a digital release so we need only front page 12x12cm
Updates
If anyone wants to remove the background from the pictures and be creative that is fine! :)
Industry/Entity Type
Digital
Colors
Designer to choose colors to be used in the design.
Look and feel
Each slider illustrates characteristics of the customer's brand and the style your logo design should communicate.

```html
<!DOCTYPE html>
<html lang="en">
<head>
<meta charset="utf-8">
<title>Mirelle – Glass Tide</title>
<link rel="stylesheet" href="https://fonts.googleapis.com/css2?family=Audiowide&family=Bungee&display=swap">
<style>
  :root {
    --page: #ffffff;
    --night: #0b0706;
    --ember: #e2561c;
    --ember-deep: #7a2a0e;
    --flame: #f39a2b;
    --flame-light: #ffd36a;
    --ink-white: #ffffff;
    --photo-dark: #1a1210;
    --photo-warm: #6b4a3a;
  }
  * { margin: 0; padding: 0; box-sizing: border-box; }
  html, body {
    width: 1200px; height: 1200px; overflow: hidden;
    background: var(--page);
  }
  .canvas { position: relative; width: 1200px; height: 1200px; background: var(--page); }
  .cover {
    position: absolute; left: 118px; top: 115px; width: 965px; height: 967px;
    background: var(--night); overflow: hidden;
  }
  .smoke-backdrop {
    position: absolute; inset: 0;
    background:
      radial-gradient(ellipse 260px 420px at 90% 35%, rgba(226,86,28,.55), transparent 70%),
      radial-gradient(ellipse 220px 360px at 6% 30%, rgba(226,86,28,.45), transparent 70%),
      radial-gradient(ellipse 200px 300px at 4% 80%, rgba(226,86,28,.35), transparent 70%),
      radial-gradient(ellipse 180px 260px at 96% 70%, rgba(226,86,28,.45), transparent 70%),
      radial-gradient(ellipse 300px 120px at 35% 2%, rgba(122,42,14,.5), transparent 70%),
      var(--night);
  }
  .artist-photo {
    position: absolute; left: 300px; top: 415px; width: 665px; height: 552px;
    background:
      radial-gradient(ellipse 150px 190px at 64% 42%, var(--photo-warm), transparent 75%),
      linear-gradient(180deg, transparent 0%, var(--photo-dark) 55%);
    border-radius: 300px 300px 0 0;
  }
  .artist-name {
    position: absolute; left: 32px; top: 50px;
    font-family: "Audiowide", sans-serif; font-size: 118px; line-height: 1;
    color: var(--flame); text-transform: lowercase; letter-spacing: 2px;
  }
  .credit {
    position: absolute; left: 40px; width: 470px; text-align: center;
    font-family: "Audiowide", sans-serif; color: var(--ink-white);
    text-transform: uppercase; line-height: 1;
  }
  .credit-label { top: 198px; font-size: 40px; }
  .credit-guest { top: 268px; font-size: 38px; }
  .title {
    position: absolute; left: 92px; top: 345px; width: 420px;
    font-family: "Bungee", sans-serif; font-size: 128px; line-height: .98;
    color: var(--flame); text-transform: lowercase; text-align: center;
  }
  .title span { display: block; }
</style>
</head>
<body>
<div class="canvas">
  <section class="cover">
    <div class="smoke-backdrop" role="img" aria-label="Swirling orange smoke on black"></div>
    <div class="artist-photo" role="img" aria-label="Portrait photo of the singer in a black jacket with long wavy hair"></div>
    <div class="artist-name">Mirelle</div>
    <p class="credit credit-label">Featuring</p>
    <p class="credit credit-guest">Tovro pip rascal</p>
    <h1 class="title"><span>Glass</span><span>Tide</span></h1>
  </section>
</div>
</body>
</html>
```